4 x Florist Footpath Signage Boards that are consistant with each other for a modern florist

Eye catching, easy to read. little bit floral.
See example attached for wording. We are a modern florist in a country town.
This will be out on the street and needs to stand out!!

The Signage Panels
1. Valentines Day - 14th Feb
2. Workshop Signage boards - see attached example
3. Mothers Day Signage Board - 'Treat mum this Mothers Day'
4. We Are Open

Attached is a copy of the design guidelines and the template. the base of the sign is white.

Target Market(s)

Modern

Industry/Entity Type

Florist

Font styles to use
Sans Serif

Colors
eea4c8
f59296
ffffff
757575

Requirements
Must have
• flowers
• weddings
• giftware
• workshops
• flowers make people happy
• hollybrookblooms.co.nz
Nice to have
• Logo
• little bit of floral or greenery
• my shop is modem and industrial
Should not have
• Needs to be able to read easy

```html
<!DOCTYPE html>
<html lang="en">
<head>
<meta charset="UTF-8">
<title>Flowers Make People Happy – Footpath Sign</title>
<link rel="stylesheet" href="https://fonts.googleapis.com/css2?family=Montserrat:wght@800&family=Barlow+Semi+Condensed:wght@500&display=swap">
<style>
  :root {
    --pink-lilac: #eea4c8;
    --pink-coral: #f59296;
    --pink-text: #e86f84;
    --white: #ffffff;
    --grey: #757575;
    --stage: #3a3b3f;
    --bloom-crimson: #b33a62;
    --bloom-blush: #f6bfc9;
    --bloom-cream: #f4ece8;
  }
  * { margin: 0; padding: 0; box-sizing: border-box; }
  html, body {
    width: 1200px; height: 675px; overflow: hidden;
    background: var(--stage);
  }
  .sign {
    position: absolute; left: 375px; top: 38px;
    width: 450px; height: 600px;
  }
  .sign-body {
    position: absolute; left: 0; top: 0; width: 450px; height: 570px;
    border-radius: 30px;
    background: linear-gradient(90deg, var(--pink-lilac), var(--pink-coral));
    overflow: hidden;
  }
  .sign-foot {
    position: absolute; left: 23px; top: 520px; width: 404px; height: 80px;
    background: linear-gradient(90deg, #efa0c0, #f4949c);
    overflow: hidden;
  }
  .floral-top {
    position: absolute; left: 0; top: 0; width: 450px; height: 100px;
    background: linear-gradient(90deg, var(--bloom-cream) 0%, var(--bloom-crimson) 22%, var(--bloom-cream) 42%, var(--bloom-blush) 62%, var(--bloom-crimson) 80%, var(--bloom-blush) 100%);
    -webkit-mask: linear-gradient(180deg, #000 55%, transparent 100%);
            mask: linear-gradient(180deg, #000 55%, transparent 100%);
  }
  .floral-bottom {
    position: absolute; left: 0; top: 496px; width: 450px; height: 104px;
    background: linear-gradient(90deg, var(--bloom-blush) 0%, var(--bloom-cream) 15%, var(--bloom-crimson) 35%, var(--bloom-cream) 52%, var(--bloom-blush) 65%, var(--bloom-crimson) 82%, var(--bloom-cream) 100%);
    -webkit-mask: linear-gradient(0deg, #000 60%, transparent 100%);
            mask: linear-gradient(0deg, #000 60%, transparent 100%);
  }
  .sign-foot .floral-bottom { left: -23px; top: -24px; }
  .hang-slot {
    position: absolute; left: 190px; top: 23px; width: 70px; height: 18px;
    border-radius: 9px; background: var(--stage);
  }
  .headline {
    position: absolute; left: 0; width: 450px; text-align: center;
    font-family: "Montserrat", sans-serif; font-weight: 800;
    color: var(--white); line-height: 1;
    text-shadow: 1px 2px 3px rgba(117,117,117,0.45);
  }
  .headline--flowers { top: 85px; font-size: 52px; }
  .headline--make { top: 134px; font-size: 52px; letter-spacing: -0.5px; }
  .headline--happy { top: 180px; font-size: 73px; }
  .services {
    position: absolute; left: 94px; top: 256px; width: 263px; height: 176px;
    background: var(--white); border-radius: 24px;
    box-shadow: 1px 3px 5px rgba(117,117,117,0.35);
  }
  .services-frame {
    position: absolute; inset: 11px; border: 2px solid var(--pink-text);
    border-radius: 15px;
  }
  .service {
    position: absolute; left: 0; width: 263px; height: 30px;
    text-align: center; line-height: 30px;
    font-family: "Barlow Semi Condensed", sans-serif; font-weight: 500;
    font-size: 28px; color: var(--pink-text);
  }
  .service::before, .service::after {
    content: ""; position: absolute; top: 7px; width: 17px; height: 17px;
    border-radius: 50%; background: var(--pink-coral);
  }
  .service::before { left: 35px; }
  .service::after { left: 209px; }
  .service--wedding { top: 16px; }
  .service--giftware { top: 54px; }
  .service--workshops { top: 94px; }
  .service--flowers { top: 132px; }
  .web-address {
    position: absolute; left: 72px; top: 452px; width: 306px; height: 37px;
    background: var(--white); border-radius: 19px;
    box-shadow: 1px 3px 5px rgba(117,117,117,0.35);
    text-align: center; line-height: 37px;
    font-family: "Barlow Semi Condensed", sans-serif; font-weight: 500;
    font-size: 24px; color: var(--pink-text);
  }
</style>
</head>
<body>
  <div class="sign">
    <div class="sign-foot">
      <div class="floral-bottom" role="img" aria-label="Peonies in crimson, blush and cream with green leaves"></div>
    </div>
    <div class="sign-body">
      <div class="floral-top" role="img" aria-label="Border of crimson, blush and cream peonies with green leaves"></div>
      <div class="floral-bottom" role="img" aria-label="Border of crimson, blush and cream peonies with green leaves"></div>
      <div class="hang-slot"></div>
      <h1 class="headline headline--flowers">FLOWERS</h1>
      <p class="headline headline--make">MAKE PEOPLE</p>
      <p class="headline headline--happy">HAPPY</p>
      <div class="services">
        <div class="services-frame"></div>
        <p class="service service--wedding">Wedding</p>
        <p class="service service--giftware">Giftware</p>
        <p class="service service--workshops">Workshops</p>
        <p class="service service--flowers">Flowers</p>
      </div>
      <p class="web-address">hollybrookblooms.co.nz</p>
    </div>
  </div>
</body>
</html>
```